Small Business Consulting Firm Needs Business Card Design

Need a sleek modern business card with 2 sides matching the colors of our logo. We will be placing these with a mailer we are sending out. These business cards will only ever be given to business owners. We operate helping businesses who are struggling with cash flow or finances. If the green and blue design needs to be moved to the right of "Harborline Crest Consulting" for aesthetic purposes that is ok. We will need an editable file if possible. We would like to include the reps name, email, website, and phone number. For now just use Peter Vance, pvance@harborlinecrest.com, www.harborlinecrest.com, and 833-555-0172.

```html
<!DOCTYPE html>
<html lang="en">
<head>
<meta charset="UTF-8">
<title>Harborline Crest Consulting – Business Card</title>
<link href="https://fonts.googleapis.com/css2?family=Montserrat:wght@400;500;600&display=swap" rel="stylesheet">
<style>
  :root {
    --page-bg: #eeeeef;
    --brand-blue: #0a72b8;
    --brand-blue-light: #0386cc;
    --brand-green: #6aab3c;
    --ink: #3a3a3c;
    --ink-soft: #4a4a4c;
    --card-white: #ffffff;
  }
  * { box-sizing: border-box; margin: 0; padding: 0; }
  html, body {
    width: 1200px; height: 900px; overflow: hidden;
    background: var(--page-bg);
    font-family: "Montserrat", Arial, sans-serif;
  }
  .stage {
    width: 1200px; height: 900px;
    display: flex; flex-direction: column; align-items: center; justify-content: center;
    gap: 48px;
  }
  .card {
    width: 620px; height: 354px;
    position: relative;
    box-shadow: 0 6px 18px rgba(0,0,0,0.12);
  }

  /* Front */
  .card-front {
    background: linear-gradient(160deg, var(--brand-blue) 0%, var(--brand-blue-light) 100%);
    color: var(--card-white);
  }
  .front-lockup {
    position: absolute; left: 0; right: 0; top: 120px;
    display: flex; align-items: center; justify-content: center; gap: 18px;
  }
  .lockup-square { width: 44px; height: 44px; background: var(--card-white); }
  .lockup-name { font-weight: 400; color: var(--card-white); line-height: 1; }
  .lockup-name .name-main { display: block; font-size: 27px; letter-spacing: 0.5px; }
  .lockup-name .name-sub { display: block; font-size: 10px; letter-spacing: 4.5px; margin-top: 6px; text-align: center; }
  .front-web {
    position: absolute; left: 0; right: 0; bottom: 40px;
    text-align: center; font-size: 14px; letter-spacing: 3.5px; font-weight: 400;
  }

  /* Back */
  .card-back { background: var(--card-white); display: flex; align-items: center; }
  .back-brand {
    width: 310px; display: flex; flex-direction: column; align-items: center;
  }
  .back-square { width: 70px; height: 70px; background: var(--brand-green); margin-bottom: 22px; }
  .back-brand .lockup-name { color: var(--ink); text-align: center; }
  .back-brand .name-main { font-size: 23px; }
  .back-brand .name-sub { font-size: 9px; letter-spacing: 4px; }
  .divider { width: 1.5px; height: 170px; background: var(--brand-blue); }
  .rep { padding-left: 22px; }
  .rep-name { font-size: 19px; font-weight: 500; color: var(--brand-blue); letter-spacing: 1px; }
  .rep-title { font-size: 13px; color: var(--ink); margin-top: 4px; }
  .contact-list { list-style: none; margin-top: 28px; }
  .contact-item {
    display: flex; align-items: center; gap: 8px;
    font-size: 15px; color: var(--ink-soft); margin-bottom: 9px;
  }
  .contact-icon { width: 16px; height: 16px; flex: none; fill: var(--brand-blue); }
</style>
</head>
<body>
<main class="stage">
  <section class="card card-front">
    <div class="front-lockup">
      <span class="lockup-square"></span>
      <span class="lockup-name">
        <span class="name-main">HARBORLINE CREST</span>
        <span class="name-sub">CONSULTING</span>
      </span>
    </div>
    <p class="front-web">WWW.HARBORLINECREST.COM</p>
  </section>

  <section class="card card-back">
    <div class="back-brand">
      <span class="back-square"></span>
      <span class="lockup-name">
        <span class="name-main">HARBORLINE CREST</span>
        <span class="name-sub">CONSULTING</span>
      </span>
    </div>
    <span class="divider"></span>
    <div class="rep">
      <h1 class="rep-name">PETER VANCE</h1>
      <p class="rep-title">CEO | Founder</p>
      <ul class="contact-list">
        <li class="contact-item">
          <svg class="contact-icon" viewBox="0 0 24 24"><path d="M6.6 10.8a15.1 15.1 0 0 0 6.6 6.6l2.2-2.2a1 1 0 0 1 1-.25 11.4 11.4 0 0 0 3.6.57 1 1 0 0 1 1 1V20a1 1 0 0 1-1 1A17 17 0 0 1 3 4a1 1 0 0 1 1-1h3.5a1 1 0 0 1 1 1c0 1.25.2 2.45.57 3.57a1 1 0 0 1-.25 1z"/></svg>
          833 555 0172
        </li>
        <li class="contact-item">
          <svg class="contact-icon" viewBox="0 0 24 24"><path d="M2 5h20v14H2z M2 5l10 7 10-7" fill="var(--brand-blue)"/><path d="M2 6l10 7 10-7" fill="none" stroke="#fff" stroke-width="1.6"/></svg>
          pvance@harborlinecrest.com
        </li>
        <li class="contact-item">
          <svg class="contact-icon" viewBox="0 0 24 24"><circle cx="12" cy="12" r="10"/><path d="M2 12h20M12 2c3 3 3 17 0 20M12 2c-3 3-3 17 0 20" fill="none" stroke="#fff" stroke-width="1.4"/></svg>
          www.harborlinecrest.com
        </li>
      </ul>
    </div>
  </section>
</main>
</body>
</html>
```